Redesign of Business Card to look more professional and stand out

Business card design. You can lean more about our company by going to dkrfabworks.example. Raised letters would be nice. Company name & Address
DK&R
418 Wendlow Ridge Drive, Suite 340
Ashbury, TN 37412

You can use my name and title: Glenn Harwick
Business Development Manager

Target Market(s)

Heavy Industrial market, i.e. utilities, chemical plants, paper mills, construction companies

Industry/Entity Type

Construction

Contact Information for Business Card

We provide Project Management & Project Support Services

Font styles to use
Serif

Requirements
Must have
• Company name & Address
• DK&R
• 418 Wendlow Ridge Drive, Suite 340
• Ashbury, TN 37412
Nice to have
• ideas for the back of the card
Should not have
• no crazy colors. needs to look professional and standout.

```html
<!DOCTYPE html>
<html lang="en">
<head>
<meta charset="utf-8">
<title>DK&amp;R Business Card</title>
<link href="https://fonts.googleapis.com/css2?family=Open+Sans:wdth,wght@75..100,400..700&display=swap" rel="stylesheet">
<style>
  :root {
    --backdrop: #948d85;
    --card: #ffffff;
    --navy: #1d3864;
    --text-gray: #6b6b6b;
    --photo-light: #f2f2f2;
    --photo-mid: #c9c9c9;
    --steel-light: #eef3f8;
    --steel-mid: #b9c7d6;
  }
  * { margin: 0; padding: 0; box-sizing: border-box; }
  html, body { width: 1200px; height: 1000px; overflow: hidden; }
  body {
    background: var(--backdrop);
    font-family: "Open Sans", Arial, sans-serif;
    position: relative;
  }
  .card {
    position: absolute;
    top: 108px;
    width: 498px;
    height: 283px;
    background: var(--card);
    overflow: hidden;
  }
  .card--front { left: 68px; }
  .card--back { left: 628px; }

  .brand-block {
    position: absolute;
    top: 0;
    height: 202px;
    background: var(--navy);
    color: #fff;
    font-weight: 700;
    font-stretch: 75%;
  }
  .card--front .brand-block { left: 0; width: 192px; }
  .card--back .brand-block { left: 309px; width: 189px; height: 200px; }

  .brand-name { position: absolute; line-height: 1; white-space: nowrap; }
  .card--front .brand-name { left: 30px; top: 25px; font-size: 70px; }
  .card--back .brand-name { left: 0; width: 100%; text-align: center; top: 53px; font-size: 40px; }

  .photo-strip { position: absolute; top: 210px; height: 73px; }
  .photo-strip--plans {
    left: 0; width: 192px;
    background: linear-gradient(120deg, var(--photo-mid), var(--photo-light) 45%, #d8d8d8 70%, var(--photo-light));
  }
  .photo-strip--pipes {
    left: 309px; width: 189px;
    background: linear-gradient(110deg, #cfd8e2, var(--steel-light) 40%, var(--steel-mid) 75%, #dfe8f1);
  }

  .services {
    position: absolute; left: 220px; top: 57px;
    color: var(--navy); font-weight: 700; font-size: 15px; line-height: 18px;
  }
  .summary {
    position: absolute; left: 219px; top: 136px; width: 210px;
    color: var(--text-gray); font-size: 13.5px; line-height: 18px;
  }
  .website {
    position: absolute; left: 221px; top: 237px;
    color: var(--navy); font-weight: 700; font-size: 15px;
  }

  .contact { position: absolute; left: 30px; top: 56px; color: var(--navy); }
  .contact__name { font-weight: 700; font-size: 15px; line-height: 18px; }
  .contact__title { font-size: 15.3px; line-height: 18px; }
  .contact__lines { margin-top: 12px; font-size: 15.3px; line-height: 18px; }
  .address {
    position: absolute; left: 30px; top: 208px;
    color: var(--text-gray); font-size: 15px; line-height: 18px;
  }
</style>
</head>
<body>
  <section class="card card--front">
    <div class="brand-block"><span class="brand-name">DK&amp;R</span></div>
    <div class="photo-strip photo-strip--plans" role="img" aria-label="Photo of rolled construction blueprints"></div>
    <p class="services">Project Management<br>&amp; Project Support Services</p>
    <p class="summary">Preconstruction planning and construction management services for the public and private sectors.</p>
    <p class="website">dkr-projectmgt.example</p>
  </section>

  <section class="card card--back">
    <div class="contact">
      <p class="contact__name">Glenn Harwick</p>
      <p class="contact__title">Business Development Manager</p>
      <p class="contact__lines">(615) 555-0148<br>harwickg@dkr-projectmgt.example</p>
    </div>
    <p class="address">418 Wendlow Ridge Drive, Suite 340<br>Ashbury, TN 37412</p>
    <div class="brand-block"><span class="brand-name">DK&amp;R</span></div>
    <div class="photo-strip photo-strip--pipes" role="img" aria-label="Photo of industrial ductwork and pipes"></div>
  </section>
</body>
</html>
```